Brightwave Business Card

Professional Business Card Design required using the attached contact information.

Contact information can be rearranged as required.

The company is a new start up venture developing solar systems, the branding should be in keeping with that of one of the investors whose website is as follows https://www.quorvex.com/

```html
<!DOCTYPE html>
<html lang="en">
<head>
<meta charset="utf-8">
<title>Brightwave Renewables – Business Card</title>
<link href="https://fonts.googleapis.com/css2?family=Open+Sans:wght@400;600;700&display=swap" rel="stylesheet">
<style>
  :root {
    --backdrop: #e6e7e7;
    --card-dark: #040708;
    --card-light: #f4f4f4;
    --brand-green: #2a6650;
    --ink: #3a3a3a;
    --white: #ffffff;
  }
  * { margin: 0; padding: 0; box-sizing: border-box; }
  html, body {
    width: 1200px;
    height: 960px;
    overflow: hidden;
    background: var(--backdrop);
    font-family: "Open Sans", Arial, sans-serif;
  }
  .canvas {
    position: relative;
    width: 1200px;
    height: 960px;
  }
  .card {
    position: absolute;
    left: 301px;
    width: 601px;
    height: 343px;
  }
  .card--front {
    top: 114px;
    background: var(--card-dark);
    display: flex;
    align-items: center;
    justify-content: center;
  }
  .brand-mark {
    display: flex;
    align-items: center;
    gap: 12px;
    margin-top: -26px;
  }
  .brand-mark__dot {
    width: 10px;
    height: 10px;
    border-radius: 50%;
    background: var(--brand-green);
  }
  .brand-mark__name {
    color: var(--white);
    font-weight: 600;
    font-size: 21px;
    letter-spacing: 2.2px;
    text-transform: uppercase;
  }
  .card--back {
    top: 509px;
    background: var(--card-light);
  }
  .holder-name {
    position: absolute;
    left: 46px;
    top: 67px;
    color: var(--brand-green);
    font-weight: 700;
    font-size: 19px;
    letter-spacing: 0.2px;
    text-transform: uppercase;
  }
  .company {
    position: absolute;
    left: 46px;
    top: 193px;
    font-size: 14.5px;
    line-height: 20px;
    color: var(--ink);
  }
  .company__name { color: var(--brand-green); }
  .contact-list {
    position: absolute;
    left: 46px;
    top: 242px;
    list-style: none;
    font-size: 14.5px;
    line-height: 20.5px;
    color: var(--ink);
  }
  .contact-list li {
    display: flex;
    align-items: center;
    gap: 5px;
  }
  .contact-list svg {
    width: 13px;
    height: 13px;
    flex: none;
  }
</style>
</head>
<body>
<main class="canvas">
  <section class="card card--front" aria-label="Card front">
    <div class="brand-mark">
      <span class="brand-mark__name">Brightwave</span>
      <span class="brand-mark__dot"></span>
      <span class="brand-mark__name">Renewables</span>
    </div>
  </section>

  <section class="card card--back" aria-label="Card back">
    <h1 class="holder-name">Daniel Harlow</h1>
    <p class="company">
      <span class="company__name">Brightwave Renewables LLC</span><br>
      218 Harbor Street, Portland, ME 04101
    </p>
    <ul class="contact-list">
      <li>
        <svg viewBox="0 0 16 16" aria-hidden="true"><path fill="#2a6650" d="M3.6 1.2l2.2 2.9c.3.4.2.9-.1 1.2L4.6 6.4c.9 2 2.6 3.8 4.9 4.9l1.1-1.1c.3-.3.9-.4 1.2-.1l2.9 2.2c.4.3.4.9.1 1.2l-1.5 1.5c-.5.5-1.3.7-2 .4C6 13.6 2.4 10 .6 4.8c-.3-.7-.1-1.5.4-2L2.4 1.1c.3-.3.9-.3 1.2.1z"/></svg>
        <span>+1 (555) 214-0938</span>
      </li>
      <li>
        <svg viewBox="0 0 16 16" aria-hidden="true"><rect x="1" y="3" width="14" height="10" fill="none" stroke="#2a6650" stroke-width="1.8"/><path d="M1.5 3.5L8 9l6.5-5.5" fill="none" stroke="#2a6650" stroke-width="1.6"/></svg>
        <span>daniel.harlow@brightwave-renewables.com</span>
      </li>
      <li>
        <svg viewBox="0 0 16 16" aria-hidden="true"><g fill="none" stroke="#2a6650" stroke-width="1.3"><circle cx="8" cy="8" r="6.5"/><ellipse cx="8" cy="8" rx="2.8" ry="6.5"/><path d="M1.5 8h13M2.5 4.8h11M2.5 11.2h11"/></g></svg>
        <span>www.brightwave-renewables.com</span>
      </li>
    </ul>
  </section>
</main>
</body>
</html>
```